Wordpress Design

Need a responsive wordpress website with the minimum 10 service description pages. This website is for a small business consultancy, providing business development and digital marketing services.

Will also need at least 4 diffrent templates: Home page, service page, Landing Page and blog.

The site will be using block editor.

Coded - Design and coding required

1 page

Sans Serif
• Segoe UI

```html
<!DOCTYPE html>
<html lang="en">
<head>
<meta charset="utf-8">
<title>Brightview Advisory – Business Consultancy</title>
<link href="https://fonts.googleapis.com/css2?family=Poppins:wght@300;400;500;600;700&display=swap" rel="stylesheet">
<style>
  :root {
    --blue: #00a8e8;
    --blue-light: #8fdcf8;
    --blue-pale: #cfeefb;
    --ink: #111111;
    --grey: #8a8a8a;
    --white: #ffffff;
    --dot: #e4e4e4;
  }
  * { margin: 0; padding: 0; box-sizing: border-box; }
  html, body { width: 1200px; height: 3375px; overflow: hidden; }
  body { position: relative; background: var(--white); font-family: "Poppins", "Segoe UI", sans-serif; color: var(--ink); }
  .abs { position: absolute; }

  /* header */
  .brand { left: 108px; top: 46px; display: flex; align-items: center; gap: 12px; }
  .brand-mark { width: 40px; height: 40px; border-radius: 50%; background: var(--blue); }
  .brand-name { font-size: 24px; font-weight: 600; color: var(--ink); letter-spacing: -0.3px; }
  .main-nav { left: 451px; top: 56px; display: flex; gap: 0; font-size: 15px; color: var(--blue); }
  .main-nav a { color: var(--blue); text-decoration: none; position: absolute; white-space: nowrap; }
  .nav-contact { background: var(--blue); color: var(--white) !important; padding: 1px 9px; border-radius: 10px; font-weight: 500; }

  /* hero */
  .hero-title { left: 106px; top: 215px; color: var(--blue); font-weight: 400; line-height: 1; }
  .hero-title .l1 { display: block; font-size: 70px; font-weight: 500; letter-spacing: 0.5px; }
  .hero-title .l2 { display: block; font-size: 53px; margin-top: 20px; }
  .hero-lead { left: 109px; top: 386px; font-size: 20px; line-height: 33px; letter-spacing: 1.2px; }
  .btn-start { left: 108px; top: 480px; width: 135px; height: 31px; border-radius: 8px; background: var(--blue); color: var(--white); font-size: 20px; text-align: center; line-height: 31px; }
  .hero-dots { left: 628px; top: 120px; width: 572px; height: 475px; border-radius: 48% 0 0 52%; background: radial-gradient(circle at 60% 50%, #ececec 0%, #f5f5f5 55%, rgba(255,255,255,0) 72%); }
  .hero-ring { left: 702px; top: 165px; width: 372px; height: 372px; border-radius: 50%; border: 6px solid var(--blue); }
  .hero-photo { left: 718px; top: 181px; width: 340px; height: 340px; border-radius: 50%; background: linear-gradient(135deg, #d8d8d8, #8b8b8b 60%, #5e5e5e); }
  .stroke { height: 18px; border-radius: 9px; background: var(--blue); transform: rotate(-35deg); }

  /* rank band */
  .rank-band { left: 0; top: 683px; width: 1200px; height: 341px; background: linear-gradient(100deg, #bcd9e4 0%, #d7e6ef 35%, #c7dae6 60%, #d9e7ee 100%); }
  .rank-title { left: 0; top: 740px; width: 1220px; text-align: center; font-size: 38px; font-weight: 700; line-height: 50px; letter-spacing: 1px; }
  .rank-sub { left: 0; top: 846px; width: 1210px; text-align: center; font-size: 16px; }
  .field { height: 52px; border-radius: 26px; background: var(--white); border: 1px solid var(--blue-pale); font-size: 15px; padding-left: 24px; line-height: 50px; color: #333; }
  .field svg { position: absolute; right: 22px; top: 15px; }
  .btn-submit { left: 797px; top: 908px; width: 218px; height: 52px; border-radius: 26px; background: var(--blue); color: var(--white); font-weight: 600; font-size: 19px; text-align: center; line-height: 52px; }

  /* services */
  .services-title { left: 0; top: 1163px; width: 1200px; text-align: center; color: var(--blue); font-size: 50px; font-weight: 600; letter-spacing: 1.5px; }
  .deco-circle { border-radius: 50%; }
  .service { width: 300px; text-align: center; }
  .service-icon { width: 80px; height: 76px; margin: 0 auto; border-radius: 8px; background: linear-gradient(135deg, var(--blue) 0%, var(--blue) 45%, #333 46%, #333 100%); opacity: 0.85; }
  .service h3 { margin-top: 24px; color: var(--blue); font-size: 14px; font-weight: 600; letter-spacing: 1.2px; }
  .service p { margin-top: 6px; font-size: 10.5px; line-height: 12px; letter-spacing: 0.3px; }
  .read-more { display: inline-block; margin-top: 18px; border: 1.5px solid #333; border-radius: 14px; padding: 3px 10px; font-size: 10.5px; letter-spacing: 0.5px; }

  /* cta */
  .cta-band { left: 0; top: 2368px; width: 1200px; height: 379px; background: var(--blue); overflow: hidden; }
  .cta-title { left: 742px; top: 2472px; transform: translateX(-50%); width: 820px; text-align: center; color: var(--white); font-size: 26px; font-weight: 600; line-height: 32px; letter-spacing: 1.4px; }
  .cta-sub { left: 742px; top: 2545px; transform: translateX(-50%); width: 700px; text-align: center; color: var(--white); font-size: 20px; letter-spacing: 1.5px; }
  .cta-pill { left: 554px; top: 2604px; width: 396px; height: 53px; border-radius: 27px; background: var(--white); }
  .cta-pill span { position: absolute; left: 24px; top: 16px; font-size: 16px; color: #333; }
  .cta-pill b { position: absolute; right: 2px; top: 2px; width: 186px; height: 49px; border-radius: 25px; background: var(--blue); color: var(--white); font-size: 19px; font-weight: 600; line-height: 49px; text-align: center; letter-spacing: 0.5px; }

  /* footer */
  .footer-brand { left: 0; top: 2882px; width: 1200px; display: flex; justify-content: center; align-items: center; gap: 14px; }
  .footer-brand .brand-mark { width: 52px; height: 52px; }
  .footer-brand .brand-name { font-size: 31px; }
  .footer-heading { top: 3047px; font-size: 24px; letter-spacing: 1.2px; }
  .ghost-input { width: 260px; height: 38px; border: 2px solid #222; border-radius: 19px; font-size: 19px; padding-left: 30px; line-height: 34px; }
  .solid-btn { width: 260px; height: 38px; border-radius: 19px; background: var(--blue); color: #111; text-align: center; font-size: 16px; line-height: 38px; letter-spacing: 1px; }
  .phone { left: 524px; top: 3108px; font-size: 19px; letter-spacing: 0.8px; }
</style>
</head>
<body>

<header>
  <div class="brand abs"><span class="brand-mark"></span><span class="brand-name">Brightview Advisory</span></div>
  <nav class="main-nav abs">
    <a style="left:0">Business Strategy</a>
    <a style="left:178px">Marketing Strategy</a>
    <a style="left:367px">Blog</a>
    <a style="left:441px">About Us</a>
    <a class="nav-contact" style="left:542px;top:-1px">Contact Us</a>
  </nav>
</header>

<section class="hero">
  <h1 class="hero-title abs"><span class="l1">Welcome to</span><span class="l2">Brightview Advisory</span></h1>
  <p class="hero-lead abs">Where your ideas meet our strategy<br>to deliver amazing results</p>
  <div class="btn-start abs">Get Start</div>
  <div class="hero-dots abs" role="img" aria-label="Soft dotted background pattern"></div>
  <div class="hero-ring abs"></div>
  <div class="hero-photo abs" role="img" aria-label="Photo of a consultant with a coffee cup working at a laptop"></div>
  <div class="stroke abs" style="left:988px;top:228px;width:110px"></div>
  <div class="stroke abs" style="left:1023px;top:246px;width:110px"></div>
  <div class="stroke abs" style="left:662px;top:437px;width:110px"></div>
  <div class="stroke abs" style="left:720px;top:449px;width:110px"></div>
</section>

<section class="rank">
  <div class="rank-band abs" role="img" aria-label="Faded photo of a person working at a laptop on a desk"></div>
  <h2 class="rank-title abs">WANT TO KNOW HOW YOU RANK<br>AGAINST COMPETITION?</h2>
  <p class="rank-sub abs">Competitor analysis helps you to understand where you stand in the market</p>
  <div class="field abs" style="left:204px;top:908px;width:304px">Enter Your Website Url
    <svg width="24" height="24" viewBox="0 0 24 24" fill="none" stroke="#555" stroke-width="1.3"><circle cx="12" cy="12" r="10"/><ellipse cx="12" cy="12" rx="4.5" ry="10"/><path d="M2 12h20M4 6.5h16M4 17.5h16"/></svg>
  </div>
  <div class="field abs" style="left:506px;top:908px;width:320px">Enter Your Email
    <svg width="30" height="22" viewBox="0 0 30 22" fill="none" stroke="#555" stroke-width="1.3" style="right:52px"><rect x="1" y="2" width="22" height="15" rx="1"/><path d="M1 2l11 9 11-9"/><circle cx="25" cy="16" r="4"/></svg>
  </div>
  <div class="btn-submit abs">SUBMIT NOW</div>
</section>

<section class="services">
  <div class="deco-circle abs" style="left:1077px;top:1050px;width:52px;height:52px;background:var(--blue-light)"></div>
  <div class="deco-circle abs" style="left:935px;top:1160px;width:222px;height:222px;background:var(--blue-light)"></div>
  <h2 class="services-title abs">OUR SERVICES</h2>

  <div class="service abs" style="left:155px;top:1440px"><div class="service-icon" role="img" aria-label="Puzzle pieces icon"></div><h3>BUSINESS STRATEGY</h3><p>Consulting and advisory<br>Strategic planning<br>Start Up consulting</p><span class="read-more">Read More</span></div>
  <div class="service abs" style="left:454px;top:1440px"><div class="service-icon" role="img" aria-label="Business report chart icon"></div><h3>BUSINESS PLAN DEVELOPMENT</h3><p>Business planning and optimisation<br>Business model auditing<br>Financial Modelling</p><span class="read-more">Read More</span></div>
  <div class="service abs" style="left:754px;top:1440px"><div class="service-icon" role="img" aria-label="Growing coin stack icon"></div><h3>PROFIT AND GROWTH IMPROVEMENT</h3><p>Operations management and<br>optimisation<br>Business process improvement</p><span class="read-more">Read More</span></div>

  <div class="service abs" style="left:155px;top:1740px"><div class="service-icon" role="img" aria-label="Marketing route planning icon"></div><h3>MARKETING STRATEGY</h3><p>Consulting and advisory<br>Brand building/strategy</p><span class="read-more" style="margin-top:30px">Read More</span></div>
  <div class="service abs" style="left:454px;top:1740px"><div class="service-icon" role="img" aria-label="Customer and gear icon"></div><h3>CUSTOMER EXPERIENCE MAPPING</h3><p>Website audit and design<br>User experience design</p><span class="read-more" style="margin-top:30px">Read More</span></div>
  <div class="service abs" style="left:754px;top:1740px"><div class="service-icon" role="img" aria-label="Megaphone and video icon"></div><h3>DIGITAL FOOTPRINT OPTIMISATION</h3><p>SEO<br>Social media<br>Content Marketing</p><span class="read-more">Read More</span></div>

  <div class="service abs" style="left:454px;top:2020px"><div class="service-icon" role="img" aria-label="Online advertising icon"></div><h3>ADVERTISING</h3><p>Display advertisement<br>Search<br>Ecommerce/Shopping<br>Video - YouTube<br>Social Media advertising</p><span class="read-more">Read More</span></div>
</section>

<section class="cta">
  <div class="cta-band abs">
    <div class="deco-circle abs" style="left:157px;top:89px;width:54px;height:54px;background:var(--blue-light);opacity:.8"></div>
    <div class="deco-circle abs" style="left:213px;top:167px;width:92px;height:92px;background:var(--blue-light);opacity:.8"></div>
    <div class="deco-circle abs" style="left:5px;top:130px;width:236px;height:236px;background:var(--blue-light);opacity:.6"></div>
  </div>
  <h2 class="cta-title abs">READY TO TRANSFORM YOUR BUSINESS PROCESS AND MARKETING EFFORT?</h2>
  <p class="cta-sub abs">Request a free assessment and get started today</p>
  <div class="cta-pill abs"><span>Request a free 30 min</span><b>CONSULTATION</b></div>
</section>

<footer>
  <div class="footer-brand abs"><span class="brand-mark"></span><span class="brand-name">Brightview Advisory</span></div>

  <h4 class="footer-heading abs" style="left:107px">NEWS LETTER</h4>
  <div class="ghost-input abs" style="left:107px;top:3110px">Email</div>
  <div class="solid-btn abs" style="left:107px;top:3164px">SUBSCRIBE</div>

  <h4 class="footer-heading abs" style="left:523px">CALL NOW ON</h4>
  <p class="phone abs">0491 570 110</p>

  <h4 class="footer-heading abs" style="left:834px">CONTACT US</h4>
  <div class="ghost-input abs" style="left:834px;top:3110px">Name</div>
  <div class="ghost-input abs" style="left:834px;top:3158px">Email</div>
  <div class="solid-btn abs" style="left:834px;top:3206px">SUBMIT</div>
</footer>

</body>
</html>
```